Vantrel Web Services

This is a new It services company operating in Perth western Australia

we need a website that is easy to navigate without a cluttered feel to it it should have the following links and pages

About Us
Services
Clients
Contact Us
MY Vantrel (login for clients)

Hi it is a web based IT services company so we would expect customers to come to the website for 2 different purposes the first is to enquire about our services and then as they become customers come to our website to manage their services so whilst they are seperate we want do not want it to look like 2 different websites

hope this helps

Hi to update this we need a home page and templates for sub pages

this is a design brief only and not the coding of the pages or building of the site

```html
<!DOCTYPE html>
<html lang="en">
<head>
<meta charset="utf-8">
<title>Vantrel Web Services</title>
<link rel="stylesheet" href="https://fonts.googleapis.com/css2?family=Lato:wght@300;400;700&family=Open+Sans:wght@400;600;700&display=swap">
<style>
:root{
  --red:#a30d10;
  --red-bright:#c4161c;
  --blue:#0a2f91;
  --ink:#222;
  --muted:#555;
  --rule:#dcdcdc;
  --panel:#efefef;
  --feature-bg:#f7f7f7;
  --footer:#2f2f2f;
  --footer-field:#262626;
  --bar:#cfcfcf;
}
*{box-sizing:border-box;margin:0;padding:0}
html,body{width:702px;height:1200px;overflow:hidden}
body{position:relative;background:#fff;font-family:"Open Sans",Arial,sans-serif;color:var(--ink)}
.abs{position:absolute}
section,header,footer{position:absolute;left:0;width:702px}

/* header */
.site-header{top:0;height:61px;background:#fff}
.brand{left:84px;top:13px;display:flex;align-items:center;gap:8px}
.brand-mark{width:36px;height:36px;border-radius:50%;background:var(--red-bright)}
.brand-name{font-family:"Open Sans",sans-serif;font-weight:700;font-size:19px;color:var(--blue);letter-spacing:1px}
.main-nav{right:92px;top:26px;display:flex;gap:18px;font-size:8px}
.main-nav a{color:var(--ink);text-decoration:none;position:relative}
.main-nav a.active{color:var(--red)}
.main-nav a.active::after{content:"";position:absolute;left:-3px;right:-3px;top:14px;height:2px;background:var(--red)}

/* hero */
.hero{top:61px;height:298px;background:#000;border-bottom:2px solid var(--red)}
.hero-visual{left:0;top:0;width:702px;height:296px;background:radial-gradient(ellipse 230px 200px at 200px 160px,#f0a43a 0%,#a65a16 30%,#3a2010 60%,#0a0606 85%),#000}
.hero-copy{left:413px;top:74px;font-family:"Lato",sans-serif}
.hero-copy .eyebrow{color:var(--red-bright);font-weight:300;font-size:27px;line-height:28px}
.hero-copy .line{color:#fff;font-weight:300;font-size:17.5px;line-height:22px}
.hero-copy .line-red{color:var(--red-bright);font-weight:300;font-size:16px;line-height:20px}
.hero-copy .tagline{color:#fff;font-size:13px;line-height:17px;margin-top:10px}
.hero-copy .tagline b{font-weight:700}
.btn{display:inline-block;color:#fff;font-family:"Open Sans",sans-serif;text-align:center}
.btn-red{background:var(--red);font-size:12px;padding:3px 9px;margin-top:10px}
.slider-arrow{top:135px;width:38px;height:30px;background:#1b1b1b;display:flex;align-items:center;justify-content:center}
.slider-arrow.prev{left:0;border-radius:0 3px 3px 0}
.slider-arrow.next{right:0;border-radius:3px 0 0 3px}

/* features */
.features{top:359px;height:151px;background:var(--feature-bg);border-bottom:1px solid #e6e6e6}
.feature{top:-22px;width:150px;text-align:center}
.feature-icon{width:56px;height:56px;margin:0 auto;border-radius:50%;background:#fff;border:1.5px solid var(--red);display:flex;align-items:center;justify-content:center}
.feature h3{font-weight:400;font-size:11.5px;margin-top:9px}
.feature p{font-size:7px;line-height:10.6px;color:var(--muted);margin-top:6px}
.btn-blue{background:var(--blue);font-size:9.5px;width:72px;height:21px;line-height:21px;margin-top:6px}

/* welcome */
.welcome{top:510px;height:137px;text-align:center}
.welcome-title{left:0;right:0;top:16px;display:flex;justify-content:center;align-items:center;gap:8px}
.welcome-title .rule{width:82px;height:1px;background:var(--rule)}
.welcome-title h2{font-weight:400;font-size:18px;color:var(--red);display:flex;align-items:center;gap:6px}
.welcome-title .brand-mark{width:26px;height:26px}
.welcome-title .brand-inline{font-weight:700;font-size:15px;color:var(--blue);letter-spacing:1px}
.welcome .lead{left:0;right:0;top:52px;font-size:10px;color:#333}
.welcome .body{left:86px;right:86px;top:70px;font-size:6.9px;line-height:12.8px;color:var(--muted)}

/* solutions */
.solutions{top:647px;height:186px;background:var(--panel)}
.section-title{font-weight:400;font-size:16px;color:var(--blue);padding-bottom:3px;border-bottom:1px solid #d4d4d4}
.solutions .section-title{left:83px;top:15px;width:268px}
.solutions .lead{left:83px;top:46px;font-size:8.8px;color:#333}
.solutions .body{left:83px;top:63px;width:268px;font-size:7px;line-height:12.8px;color:var(--muted)}
.checks{left:82px;top:120px;list-style:none;font-size:7.4px;font-weight:600;color:#333}
.checks li{display:flex;align-items:center;gap:6px;height:15px}
.solutions-visual{left:372px;top:26px;width:248px;height:146px;border-radius:6px 6px 2px 2px;background:linear-gradient(135deg,#cfd3d6 0%,#8d949a 45%,#2a2c30 100%)}

/* testimonials & news */
.columns{top:833px;height:188px}
.columns .section-title{font-size:15.5px}
.clients .section-title{left:83px;top:14px;width:253px}
.news .section-title{left:365px;top:14px;width:254px}
.quote{left:82px;width:255px;display:flex;gap:9px;padding-bottom:10px;border-bottom:1px dashed #e2e2e2}
.avatar{width:58px;height:45px;flex:none;border:2px solid #fff;box-shadow:0 0 0 1px #ddd;background:linear-gradient(180deg,#d8d2cc,#a9a19a)}
.quote h4,.post h4{font-size:7.4px;font-weight:700}
.quote .date{font-size:7px;color:var(--blue)}
.quote p,.post p{font-size:7px;line-height:10px;color:var(--muted)}
.post{left:365px;width:255px;padding-bottom:9px;border-bottom:1px dashed #e2e2e2}
.post .date{display:flex;align-items:center;gap:5px;font-size:7.4px;font-weight:700;color:#444;margin-bottom:3px}
.post .body{padding-left:11px}
.post .headline{font-size:7px;font-weight:700;color:#333}
.read-all{font-size:7px;font-weight:700;color:var(--red);top:162px}
.col-divider{left:350px;top:48px;width:1px;height:115px;background:linear-gradient(#fff,#e3e3e3,#fff)}

/* contact footer */
.contact{top:1021px;height:145px;background:var(--footer);color:#fff}
.contact h3{font-weight:400;font-size:12.5px}
.contact-info{left:83px;top:18px}
.map-texture{left:140px;top:16px;width:140px;height:95px;background:radial-gradient(ellipse at center,#3c3c3c,transparent 70%)}
.info-row{display:flex;gap:9px;align-items:flex-start;font-size:7.4px;line-height:11px;margin-top:8px}
.info-row .ico{width:16px;display:flex;justify-content:center;flex:none}
.info-row .dot{width:18px;height:18px;border-radius:50%;background:var(--red-bright)}
.info-row b{font-weight:700}
.message-form{left:350px;top:18px;width:270px}
.field{border:1px solid #5a5a5a;background:var(--footer-field);color:#bbb;font-size:6.8px;padding:4px 7px}
.field-row{display:flex;gap:6px;margin-top:6px}
.field-row .field{flex:1;height:17px}
.field.message{height:40px;margin-top:6px}
.btn-send{float:right;margin-top:6px;width:131px;height:18px;background:var(--blue);font-size:9.5px;display:flex;align-items:center;justify-content:center;gap:7px}

/* bottom bar */
.bottom-bar{top:1166px;height:34px;background:var(--bar)}
.social{left:83px;top:8px;display:flex;gap:7px}
.social span{width:18px;height:18px;border-radius:50%;background:#e4e4e4;border:1px solid #b5b5b5}
.social span.on{background:var(--red);border-color:var(--red)}
.copyright{right:83px;top:12px;font-size:6.8px;color:#333}
</style>
</head>
<body>

<header class="site-header">
  <div class="abs brand"><span class="brand-mark"></span><span class="brand-name">Vantrel</span></div>
  <nav class="abs main-nav">
    <a class="active" href="#">Home</a><a href="#">About Us</a><a href="#">Services</a><a href="#">Clients</a><a href="#">Contact Us</a><a href="#">MY Vantrel</a>
  </nav>
</header>

<section class="hero">
  <div class="abs hero-visual" role="img" aria-label="Glowing smartphone held in a hand, surrounded by network icons, on a dark background"></div>
  <div class="abs slider-arrow prev"><svg width="10" height="12" viewBox="0 0 10 12"><path d="M8 1 3 6l5 5" fill="none" stroke="#fff" stroke-width="2.5"/></svg></div>
  <div class="abs slider-arrow next"><svg width="10" height="12" viewBox="0 0 10 12"><path d="M2 1l5 5-5 5" fill="none" stroke="#fff" stroke-width="2.5"/></svg></div>
  <div class="abs hero-copy">
    <div class="eyebrow">WE ARE</div>
    <div class="line">A WEB BASED IT SERVICE</div>
    <div class="line-red">COMPANY</div>
    <div class="tagline">We are Specializing in <b>Enterprise<br>Solutions &amp; Data Management</b></div>
    <span class="btn btn-red">Learn More</span>
  </div>
</section>

<section class="features">
  <div class="abs feature" style="left:88px">
    <div class="feature-icon"><svg width="30" height="22" viewBox="0 0 30 22" fill="#a30d10"><circle cx="7" cy="5" r="3"/><circle cx="23" cy="5" r="3"/><circle cx="15" cy="4" r="3.5"/><path d="M2 17c0-5 2-8 5-8s5 3 5 8zM18 17c0-5 2-8 5-8s5 3 5 8zM9 20c0-7 2.5-11 6-11s6 4 6 11z"/></svg></div>
    <h3>Enterprise Solutions</h3>
    <p>Lorem ipsum dolor sit amet, con adipiscing elit, sed diam nonummy nibh euis tincidunt Ut wisi enim veniam, quis nostrud ex tation ullamco suscipit lobortis nisl ut.</p>
    <span class="btn btn-blue">Learn More</span>
  </div>
  <div class="abs feature" style="left:275px">
    <div class="feature-icon"><svg width="24" height="24" viewBox="0 0 24 24" fill="#a30d10"><circle cx="12" cy="9" r="5"/><path d="M5 9a7 7 0 0 1 14 0" fill="none" stroke="#a30d10" stroke-width="1.6"/><rect x="3.5" y="8" width="3" height="5" rx="1"/><rect x="17.5" y="8" width="3" height="5" rx="1"/><path d="M3 24c0-5 4-8 9-8s9 3 9 8z"/></svg></div>
    <h3>On-site Consulting</h3>
    <p>Lorem ipsum dolor sit amet, con adipiscing elit, sed diam nonummy nibh euis tincidunt Ut wisi enim veniam, quis nostrud ex tation ullamco suscipit lobortis nisl ut.</p>
    <span class="btn btn-blue">Learn More</span>
  </div>
  <div class="abs feature" style="left:463px">
    <div class="feature-icon"><svg width="28" height="26" viewBox="0 0 28 26"><path d="M7 13a5 5 0 0 1 1-10 6 6 0 0 1 11 1 4.5 4.5 0 0 1 2 9z" fill="#a30d10"/><path d="M14 13v11M9 15v5M19 15v5M5 15v3M23 15v3" stroke="#a30d10" stroke-width="1.3"/></svg></div>
    <h3>Data Management</h3>
    <p>Lorem ipsum dolor sit amet, con adipiscing elit, sed diam nonummy nibh euis tincidunt Ut wisi enim veniam, quis nostrud ex tation ullamco suscipit lobortis nisl ut.</p>
    <span class="btn btn-blue">Learn More</span>
  </div>
</section>

<section class="welcome">
  <div class="abs welcome-title">
    <span class="rule"></span>
    <h2>Welcome to <span class="brand-mark"></span><span class="brand-inline">Vantrel</span></h2>
    <span class="rule"></span>
  </div>
  <p class="abs lead">Lorem ipsum dolor sit amet, consectetuer adipiscing elit, sed diam nonummy.</p>
  <p class="abs body">Sed diam nonummy nibh euismod tincidunt ut laoreet dolore magna aliquam erat volutpat. Ut wisi enim ad minim veniam, quis nostrud exerci tation ullamco suscipit lobortis nisl ut aliquip ex ea commodo consequat. Duis autem vel eum iriure dolor in hendrerit in vulputate velit esse molestie consequat, vel illum dolore eu feugiat nulla facilisis at vero eros et accumsan et iusto odio dignissim qui blandit praesent luptatum zzril delenit augue duis dolore te feugait facilisi. Lorem ipsum dolor sit amet, consectetuer adipiscing elit.</p>
</section>

<section class="solutions">
  <h2 class="abs section-title">Our Solutions</h2>
  <p class="abs lead">Lorem ipsum dolor sit amet, consectetuer elit, nonummy.</p>
  <p class="abs body">consectetuer adipiscing elit, sed diam nonummy.Sed diam nonummy euismod tincidunt ut laoreet dolore magna aliquam erat volutpat. Ut wisi enim veniam, quis nostrud exerci tation ullamco suscipit lobortis nisl ut aliquip ex commod consequat. Duis autem vel eum iriure dolor in hendrerit in vulputate</p>
  <ul class="abs checks">
    <li><svg width="9" height="8" viewBox="0 0 9 8"><path d="M1 4l2.5 3L8 1" fill="none" stroke="#222" stroke-width="1.4"/></svg>Duis autem vel eum iriure</li>
    <li><svg width="9" height="8" viewBox="0 0 9 8"><path d="M1 4l2.5 3L8 1" fill="none" stroke="#222" stroke-width="1.4"/></svg>Magna aliquam erat volutpat</li>
    <li><svg width="9" height="8" viewBox="0 0 9 8"><path d="M1 4l2.5 3L8 1" fill="none" stroke="#222" stroke-width="1.4"/></svg>Dolor in hendrerit in vulputate velit</li>
  </ul>
  <div class="abs solutions-visual" role="img" aria-label="Laptop showing a businessman drawing a cloud network diagram"></div>
</section>

<section class="columns">
  <h2 class="abs section-title clients" style="left:83px;top:14px;width:253px">Our Client Says</h2>
  <div class="abs quote" style="top:48px">
    <div class="avatar" role="img" aria-label="Client portrait"></div>
    <div><h4>Miss. Lina Marsh</h4><div class="date">January 1, 2014</div><p>Duis autem vel eum iriure dolor,sed di nonummy nibh euismod tincidunt ut laoreet dolore volutpat.</p></div>
  </div>
  <div class="abs quote" style="top:105px">
    <div class="avatar" role="img" aria-label="Client portrait"></div>
    <div><h4>Mr. Owen Hale</h4><div class="date">January 1, 2014</div><p>Duis autem vel eum iriure dolor,sed di nonummy nibh euismod tincidunt ut laoreet dolore volutpat.</p></div>
  </div>
  <span class="abs read-all" style="left:302px">Read all »</span>

  <div class="abs col-divider"></div>

  <h2 class="abs section-title" style="left:365px;top:14px;width:254px">Latest News</h2>
  <div class="abs post" style="top:46px">
    <div class="date"><svg width="8" height="8" viewBox="0 0 8 8"><rect x=".5" y="1" width="7" height="6.5" fill="none" stroke="#a30d10"/><rect x=".5" y="1" width="7" height="2" fill="#a30d10"/></svg>March 3, 2014</div>
    <div class="body"><div class="headline">Exerci tation ullamcorper suscipit lobortis nisl ut aliquip.</div><p>Lorem ipsum dolor sit amet, consectetuer adipiscing elit, sed di nonummy nibh euismod tincidunt ut laoreet dolore ma aliquam volutpat.</p></div>
  </div>
  <div class="abs post" style="top:103px">
    <div class="date"><svg width="8" height="8" viewBox="0 0 8 8"><rect x=".5" y="1" width="7" height="6.5" fill="none" stroke="#a30d10"/><rect x=".5" y="1" width="7" height="2" fill="#a30d10"/></svg>March 24, 2014</div>
    <div class="body"><div class="headline">Exerci tation ullamcorper suscipit lobortis nisl ut aliquip.</div><p>Lorem ipsum dolor sit amet, consectetuer adipiscing elit, sed di nonummy nibh euismod tincidunt ut laoreet dolore ma aliquam volutpat.</p></div>
  </div>
  <span class="abs read-all" style="left:585px">Read all »</span>
</section>

<footer class="contact">
  <div class="abs map-texture" role="img" aria-label="Faint dotted world map"></div>
  <div class="abs contact-info">
    <h3>Contact Info</h3>
    <div class="info-row"><span class="ico"><span class="dot"></span></span><span><b>Vantrel</b><br>sed di nonummy, nibh euismod<br>tincidunt ut laoreet.</span></div>
    <div class="info-row"><span class="ico"><svg width="10" height="10" viewBox="0 0 10 10"><path d="M2 0.5 4 3 3 4.3c.6 1.2 1.5 2.1 2.7 2.7L7 6l2.5 2L8.3 9.5C4 9 1 6 .5 1.7z" fill="#fff"/></svg></span><b>(08) 5550 1427</b></div>
    <div class="info-row"><span class="ico"><svg width="11" height="8" viewBox="0 0 11 8"><rect x=".5" y=".5" width="10" height="7" fill="none" stroke="#fff"/><path d="M.5.5 5.5 4.5 10.5.5" fill="none" stroke="#fff"/></svg></span>info@vantrel.com</div>
  </div>
  <div class="abs message-form">
    <h3>Send us a Message</h3>
    <div class="field-row"><div class="field">Name</div><div class="field">Email address</div></div>
    <div class="field message">Message</div>
    <span class="btn btn-send">Submit Your Message <svg width="12" height="12" viewBox="0 0 12 12"><circle cx="6" cy="6" r="5" fill="none" stroke="#fff" stroke-width="1.3"/><path d="M5 3.5 7.5 6 5 8.5" fill="none" stroke="#fff" stroke-width="1.3"/></svg></span>
  </div>
</footer>

<div class="abs bottom-bar" style="left:0;width:702px">
  <div class="abs social"><span class="on"></span><span></span><span></span><span></span></div>
  <div class="abs copyright">© 2014 Vantrel. All Rights Reserved.</div>
</div>

</body>
</html>
```